Criminal Defense Firm looking for an edge in business card design

Established Criminal Defense Firm looking to refresh business card. We already have logo and website, but our business cards are extremely boring. We would like to also have something on the backside of card.
Needs to be business oriented, but creative.
We provide services to professionals such as doctors, lawyers, politicians, etc.
Our specialty is to protect professional licenses when facing a criminal matter.

Update on March 10, 2015: This project is for a Business Card Design. The winner in this project will be assigned the next (1on1) project which incidentally is also entitled Business Card Design. I'm sorry for this confusion. The 1on1 project will not be for Business Card Design but will be for Stationery-Envelope Design. Thank you for your attention and continued participation.

Target Market(s)

People accused of a crime

Industry/Entity Type

Business

Contact Information for Business Card

Simple, strong, professional

Colors
85abd2
3176b5
0355a3

```html
<!DOCTYPE html>
<html lang="en">
<head>
<meta charset="utf-8">
<title>Whitcombe Alder – Business Cards</title>
<link rel="stylesheet" href="https://fonts.googleapis.com/css2?family=Sorts+Mill+Goudy:ital@0;1&family=Jost:wght@400;600&display=swap">
<style>
  :root {
    --backdrop: #e4e4e6;
    --card-back: #a9bedb;
    --card-front: #f2f1ef;
    --ink: #2a2a2e;
    --ink-soft: #3a3a40;
    --highlight: #dcdde2;
    --monogram: #dfe6f0;
    --white: #ffffff;
    --shadow: rgba(0, 0, 0, 0.12);
  }
  * { box-sizing: border-box; margin: 0; padding: 0; }
  html, body {
    width: 1200px; height: 845px; overflow: hidden;
    background: var(--backdrop);
  }
  .sheet {
    position: relative; width: 1200px; height: 845px;
    display: flex; align-items: center; justify-content: center; gap: 60px;
  }
  .card {
    position: relative; width: 490px; height: 280px;
    box-shadow: 0 6px 18px var(--shadow);
    overflow: hidden;
  }

  /* Contact side */
  .card--contact {
    background: var(--card-back);
    font-family: "Sorts Mill Goudy", Georgia, serif;
    color: var(--ink);
    text-align: center;
    padding-top: 34px;
  }
  .contact__name { font-size: 22px; font-weight: 700; letter-spacing: 0.3px; }
  .contact__role { font-style: italic; color: var(--white); font-size: 14px; margin-top: 2px; }
  .contact__web { font-size: 16px; margin-top: 20px; }
  .contact__email { font-size: 16px; margin-top: 18px; }
  .contact__address { font-size: 16px; margin-top: 18px; text-transform: uppercase; line-height: 1.2; letter-spacing: 0.4px; }
  .contact__phones { font-size: 16px; line-height: 1.2; }

  /* Firm side */
  .card--firm {
    background: var(--card-front);
    color: var(--ink);
  }
  .firm__mark {
    position: absolute; right: 40px; top: 20px;
    width: 200px; height: 200px;
    background: var(--monogram);
  }
  .firm__name {
    position: absolute; left: 28px; top: 40px;
    font-family: "Sorts Mill Goudy", Georgia, serif;
    font-size: 27px; letter-spacing: 1.2px; text-transform: uppercase;
    background: var(--highlight); padding: 2px 8px 0; line-height: 1.1;
  }
  .firm__tagline {
    position: absolute; left: 36px; right: 30px; top: 112px;
    font-family: "Jost", Futura, sans-serif;
    font-size: 15.5px; letter-spacing: 0.6px; line-height: 1.35;
    color: var(--ink-soft); text-align: center;
  }
  .firm__tagline strong { font-weight: 600; color: var(--ink); }
  .firm__phone {
    position: absolute; right: 48px; bottom: 52px;
    font-family: "Sorts Mill Goudy", Georgia, serif;
    font-size: 21px; letter-spacing: 0.8px;
    background: var(--highlight); padding: 2px 8px 0;
  }
</style>
</head>
<body>
  <main class="sheet">
    <section class="card card--contact" aria-label="Attorney contact side">
      <p class="contact__name">Daniel Whitcombe,</p>
      <p class="contact__role">Attorney at Law</p>
      <p class="contact__web">wacriminaldefense.com</p>
      <p class="contact__email">daniel@wacriminaldefense.com</p>
      <p class="contact__address">1870 Granite Avenue, Suite 210<br>Lindenport, California 95012</p>
      <p class="contact__phones">t: 555-410-2870; f: 555-410-2871</p>
    </section>

    <section class="card card--firm" aria-label="Firm side">
      <div class="firm__mark" aria-hidden="true"></div>
      <h1 class="firm__name">Whitcombe Alder</h1>
      <p class="firm__tagline">The criminal defense attorneys you want when it matters <strong>most.</strong></p>
      <p class="firm__phone">t: 555-410-2870</p>
    </section>
  </main>
</body>
</html>
```